Square Business Cards for Our Restaurant / Event Venue

We need square business cards designed for the management team of our event venue and restaurant. On one side of the card should be the the Harbor Lantern 7 logo and URL www.harborlantern7.example. On the other side should be the Ember Logo and URL www.emberhall7.example. All employee details should be on the side with Ember logo. There will be a total of 5 cards to be created with the design.

Clara Bennquist
clara@harborlantern7.example

main 555.418.3072
direct 555.730.2946

4831 West Orchard Lane SE
Washington, DC 90417

Industry/Entity Type

Business

```html
<!DOCTYPE html>
<html lang="en">
<head>
<meta charset="utf-8">
<title>Square Business Cards – Ember &amp; Harbor Lantern 7</title>
<link rel="stylesheet" href="https://fonts.googleapis.com/css2?family=Oswald:wght@600&family=Roboto:wght@400;500&display=swap">
<style>
  :root {
    --backdrop: #dde1e5;
    --paper: #efefef;
    --ink: #1c1c1c;
    --brand-red: #b3252b;
    --rule-red: #c0464a;
  }
  * { box-sizing: border-box; margin: 0; padding: 0; }
  html, body { width: 1200px; height: 1200px; overflow: hidden; }
  body {
    background: radial-gradient(circle at 50% 40%, #eef0f2 0%, var(--backdrop) 75%);
    font-family: "Roboto", Arial, sans-serif;
    color: var(--ink);
    position: relative;
  }
  .card {
    position: absolute;
    top: 340px;
    width: 520px;
    height: 520px;
    background: var(--paper);
    border-radius: 48px;
    box-shadow: 0 10px 28px rgba(60, 70, 80, 0.22);
  }
  .card--contact { left: 50px; }
  .card--venue { left: 630px; }

  /* Contact side */
  .contact {
    position: absolute;
    top: 70px;
    left: 0;
    width: 100%;
    text-align: center;
  }
  .contact__name {
    font-family: "Oswald", "Arial Narrow", sans-serif;
    font-weight: 600;
    font-size: 34px;
    letter-spacing: 0.5px;
    color: var(--brand-red);
    text-transform: uppercase;
    line-height: 1.1;
  }
  .contact__rule {
    width: 380px;
    height: 1px;
    margin: 10px auto 14px;
    background: var(--rule-red);
  }
  .contact__line {
    font-size: 20px;
    line-height: 1.4;
  }
  .contact__line--gap { margin-top: 8px; }
  .contact__label {
    color: var(--brand-red);
    font-weight: 500;
    margin-right: 6px;
  }
  .wordmark {
    position: absolute;
    left: 0;
    width: 100%;
    bottom: 46px;
    text-align: center;
    font-family: "Roboto", Arial, sans-serif;
    font-weight: 500;
    font-size: 96px;
    line-height: 1;
    color: var(--ink);
  }

  /* Venue side */
  .venue-mark {
    position: absolute;
    top: 60px;
    left: 0;
    width: 100%;
    display: flex;
    flex-direction: column;
    align-items: center;
  }
  .venue-mark__disc { display: block; }
  .venue-mark__name {
    margin-top: 20px;
    font-family: "Roboto", Arial, sans-serif;
    font-weight: 500;
    font-size: 38px;
    color: var(--brand-red);
  }
  .venue-url {
    position: absolute;
    right: 44px;
    bottom: 44px;
    font-size: 17px;
    color: var(--ink);
  }
  .venue-url__domain { color: var(--brand-red); }
</style>
</head>
<body>
  <section class="card card--contact">
    <div class="contact">
      <h1 class="contact__name">Clara Bennquist</h1>
      <div class="contact__rule"></div>
      <p class="contact__line">4831 West Orchard Lane SE</p>
      <p class="contact__line">Washington, DC 90417</p>
      <p class="contact__line contact__line--gap">www.emberhall7.example</p>
      <p class="contact__line">clara@harborlantern7.example</p>
      <p class="contact__line contact__line--gap"><span class="contact__label">Main:</span>555.418.3072</p>
      <p class="contact__line"><span class="contact__label">Direct:</span>555.730.2946</p>
    </div>
    <div class="wordmark">Ember</div>
  </section>

  <section class="card card--venue">
    <div class="venue-mark">
      <svg class="venue-mark__disc" width="220" height="220" viewBox="0 0 220 220" aria-hidden="true">
        <circle cx="110" cy="110" r="110" fill="var(--brand-red)"/>
      </svg>
      <div class="venue-mark__name">Harbor Lantern 7</div>
    </div>
    <p class="venue-url">www.<span class="venue-url__domain">harborlantern7.example</span></p>
  </section>
</body>
</html>
```